Rack Card for Portuguese Walking Food Tour

I would like a vertical rack card measuring 99x210mm. Here is the information I would like to include. It does not need to be in this format. We are located in Setubal, Portugal.
Please use the attached Teal Heron Logo.
Setúbal: Tradition and Today
Experience the culinary delights of Setúbal, Portugal with a walking food tour around our waterfront village. Discover the Mercado da Gaivota Branca, voted one of the world’s best markets by Metro Ledger, and indulge in local wines and dishes. Prepare for a calm stroll on flat streets. No hills to climb on this tour.
Duration: 4 hours
www.brinebasketwalks.com
+351 265 000 487

```html
<!DOCTYPE html>
<html lang="en">
<head>
<meta charset="utf-8">
<title>Setúbal Walking Food Tour – Rack Card</title>
<link href="https://fonts.googleapis.com/css2?family=Poppins:wght@500;600;700;800&display=swap" rel="stylesheet">
<style>
:root{
  --orange:#f26522;
  --grey:#5f6062;
  --ink:#1d1d1f;
  --paper:#f6f6f6;
  --bg:#ffffff;
}
*{margin:0;padding:0;box-sizing:border-box}
html,body{width:673px;height:1200px;overflow:hidden;background:var(--bg)}
body{font-family:'Poppins',sans-serif;position:relative}
.card{position:absolute;top:324px;width:261px;height:552px;background:var(--paper);overflow:hidden;box-shadow:0 6px 22px rgba(0,0,0,.28)}
.card--front{left:50px}
.card--back{left:362px}
.brand{height:88px;display:flex;align-items:center;justify-content:center;gap:9px}
.brand__dot{width:30px;height:30px;border-radius:50%;background:var(--orange)}
.brand__name{font-weight:600;font-size:18px;color:var(--grey);letter-spacing:.2px}
.photo{position:relative;overflow:hidden}
.photo--fish{height:227px;background:linear-gradient(160deg,#c9705a 0%,#e59a83 35%,#b5523f 65%,#7fb2ad 100%)}
.photo--breakfast{height:254px;background:linear-gradient(180deg,#6f8fb0 0%,#3d5e7a 35%,#c89a4e 65%,#e2b23a 80%,#4a4136 100%)}
.photo__edge{position:absolute;left:0;bottom:0;width:261px;height:44px;display:block}
.front-body{text-align:center;padding-top:14px}
.title{font-weight:800;font-size:44px;line-height:1;color:var(--orange);letter-spacing:-.5px}
.subtitle{font-weight:700;font-size:17.5px;line-height:1.1;color:var(--grey);margin-top:2px}
.rule{width:204px;height:1.5px;background:var(--orange);margin:7px auto 8px}
.lede{font-weight:600;font-size:12.4px;line-height:1.22;color:var(--ink)}
.duration{font-weight:700;font-size:21px;color:var(--ink);text-align:center;letter-spacing:.2px}
.duration span{color:var(--orange)}
.card--front .duration{margin-top:10px}
.footer{position:absolute;left:0;right:0;bottom:0;height:54px;background:var(--grey)}
.phone{position:absolute;left:50%;transform:translateX(-50%);bottom:40px;width:197px;height:27px;border-radius:14px;background:var(--orange);color:#fff;font-weight:700;font-size:22px;line-height:27px;text-align:center;z-index:2;letter-spacing:.2px}
.web{position:absolute;left:0;right:0;bottom:16px;text-align:center;color:#fff;font-weight:600;font-size:9px;letter-spacing:3.2px}
.includes{font-weight:700;font-size:18.5px;text-align:center;color:var(--grey);margin-top:14px}
.includes span{color:var(--orange)}
.list{list-style:none;padding:0 18px 0 18px;margin-top:6px}
.list li{position:relative;padding-left:13px;font-weight:600;font-size:9.6px;line-height:1.18;color:var(--ink);margin-bottom:9px}
.list li svg{position:absolute;left:0;top:1.5px;width:8px;height:8px}
.notice{margin:4px auto 0;width:224px;height:20px;border-radius:4px;background:var(--grey);color:#fff;font-weight:700;font-size:11.6px;line-height:20px;text-align:center}
.card--back .duration{margin-top:7px}
</style>
</head>
<body>

<article class="card card--front">
  <header class="brand">
    <span class="brand__dot"></span>
    <span class="brand__name">Brine Basket Walks</span>
  </header>
  <div class="photo photo--fish" role="img" aria-label="Photo of fresh red mullet piled on ice at a fish market">
    <svg class="photo__edge" viewBox="0 0 261 44" preserveAspectRatio="none" aria-hidden="true">
      <path d="M0 18 Q130.5 62 261 18 L261 44 L0 44Z" fill="var(--paper)"/>
      <path d="M0 6 Q130.5 46 261 6" fill="none" stroke="var(--orange)" stroke-width="5"/>
      <path d="M0 13 Q130.5 55 261 13" fill="none" stroke="var(--grey)" stroke-width="5"/>
    </svg>
  </div>
  <section class="front-body">
    <h1 class="title">SETÚBAL</h1>
    <p class="subtitle">TRADITION AND TODAY</p>
    <div class="rule"></div>
    <p class="lede">Experience the culinary delights<br>of Setúbal, Portugal</p>
    <p class="duration">DURATION: <span>4 HOURS</span></p>
  </section>
  <div class="phone">351 265 000 487</div>
  <footer class="footer"><p class="web">www.brinebasketwalks.com</p></footer>
</article>

<article class="card card--back">
  <div class="photo photo--breakfast" role="img" aria-label="Photo of a breakfast table with orange juice, fruit and pastries overlooking a bay">
    <svg class="photo__edge" viewBox="0 0 261 44" preserveAspectRatio="none" aria-hidden="true">
      <path d="M0 18 Q130.5 62 261 18 L261 44 L0 44Z" fill="var(--paper)"/>
      <path d="M0 6 Q130.5 46 261 6" fill="none" stroke="var(--orange)" stroke-width="5"/>
      <path d="M0 13 Q130.5 55 261 13" fill="none" stroke="var(--grey)" stroke-width="5"/>
    </svg>
  </div>
  <h2 class="includes">THIS <span>INCLUDES</span></h2>
  <ul class="list">
    <li><svg viewBox="0 0 8 8"><circle cx="4" cy="4" r="4" fill="#f26522"/><path d="M2.2 4.1 3.5 5.3 5.8 2.8" fill="none" stroke="#fff" stroke-width="1"/></svg>A walking food tour around our waterfront village.</li>
    <li><svg viewBox="0 0 8 8"><circle cx="4" cy="4" r="4" fill="#f26522"/><path d="M2.2 4.1 3.5 5.3 5.8 2.8" fill="none" stroke="#fff" stroke-width="1"/></svg>Discover the Mercado da Gaivota Branca, voted one of the world’s best markets by Metro Ledger.</li>
    <li><svg viewBox="0 0 8 8"><circle cx="4" cy="4" r="4" fill="#f26522"/><path d="M2.2 4.1 3.5 5.3 5.8 2.8" fill="none" stroke="#fff" stroke-width="1"/></svg>Indulge in local wines and dishes.</li>
    <li><svg viewBox="0 0 8 8"><circle cx="4" cy="4" r="4" fill="#f26522"/><path d="M2.2 4.1 3.5 5.3 5.8 2.8" fill="none" stroke="#fff" stroke-width="1"/></svg>Prepare for a calm stroll on flat streets.</li>
  </ul>
  <p class="notice">NO HILLS TO CLIMB ON THIS TOUR.</p>
  <p class="duration">DURATION: <span>4 HOURS</span></p>
  <div class="phone">351 265 000 487</div>
  <footer class="footer"><p class="web">www.brinebasketwalks.com</p></footer>
</article>

</body>
</html>
```